Business Card and Letterhead for Nurlo - modern real estate business

I need a double sided business card design for Nurlo. Please see business card brief here https://papers.trelvimo.net/sheet/q/7XrTbaLeZpMmQ2uWvd9HkCj4yNoEfsGi3lRtAz_pk/view?mode=shared

Please feel free to design the business cards however you feel best. I am happy to give some creative freedoms and then provide feedback from there.

Please then also create a letterhead to match the business card design

Colors

Designer to choose colors to be used in the design.

Requirements
Must have
• Must be a modern, elegant business card which looks very professional

```html
<!DOCTYPE html>
<html lang="en">
<head>
<meta charset="utf-8">
<title>Nurlo Business Card</title>
<link rel="stylesheet" href="https://fonts.googleapis.com/css2?family=Arimo:wght@700&family=Hind:wght@500;600&display=swap">
<style>
  :root {
    --ink: #000000;
    --brand-red: #f50606;
    --paper: #ffffff;
    --stripe: #262626;
    --photo-green: #7d9a58;
    --photo-sky: #c9d4c2;
  }
  * { margin: 0; padding: 0; box-sizing: border-box; }
  html, body { width: 969px; height: 1200px; overflow: hidden; background: var(--paper); }
  .canvas { position: relative; width: 969px; height: 1200px; }
  .shapes { position: absolute; inset: 0; width: 969px; height: 1200px; }
  .label {
    position: absolute; transform: translateY(-50%);
    line-height: 1; white-space: nowrap; color: var(--paper);
  }
  .brand-name { font-family: "Arimo", Arial, sans-serif; font-weight: 700; color: var(--brand-red); letter-spacing: 2px; }
  .tagline { font-family: "Arimo", Arial, sans-serif; font-weight: 700; }
  .front-brand { left: 0; width: 969px; text-align: center; top: 261px; font-size: 147px; }
  .front-tagline { left: 0; width: 969px; text-align: center; top: 355px; font-size: 37px; }
  .agent-name { left: 119px; top: 714px; font-family: "Hind", sans-serif; font-weight: 600; font-size: 56px; }
  .agent-role { left: 119px; top: 757px; font-family: "Hind", sans-serif; font-weight: 500; font-size: 31px; }
  .back-brand { left: 592px; top: 714px; font-size: 76px; }
  .back-tagline { left: 594px; top: 766px; font-size: 22px; }
  .contact { left: 649px; font-family: "Hind", sans-serif; font-weight: 600; font-size: 28px; letter-spacing: 0.5px; }
  .contact-phone { top: 849px; }
  .contact-email { top: 921px; }
  .contact-box { top: 952px; }
  .contact-place { top: 1014px; }
  .contact-web { top: 1102px; }
</style>
</head>
<body>
<div class="canvas">
  <svg class="shapes" viewBox="0 0 1052 1303" preserveAspectRatio="none">
    <!-- front side -->
    <rect class="front-bg" x="0" y="0" width="1052" height="650" fill="var(--ink)"/>
    <polygon class="front-red-band" points="0,497 620,497 542,578 0,578" fill="var(--brand-red)"/>
    <polygon class="front-white-band" points="0,578 542,578 575,545 825,545 865,506 930,506 930,650 0,650" fill="var(--paper)"/>
    <polygon class="front-dark-stripe" points="910,505 1052,370 1052,392 930,505" fill="var(--stripe)"/>
    <polygon class="front-red-corner" points="778,650 1052,392 1052,650" fill="var(--brand-red)"/>

    <!-- back side -->
    <rect class="back-bg" x="0" y="652" width="1052" height="651" fill="var(--ink)"/>
    <polygon class="back-dark-stripe" points="0,1020 140,1155 120,1155 0,1040" fill="var(--stripe)"/>
    <polygon class="back-white-band" points="120,1155 185,1155 225,1195 480,1195 510,1230 1052,1230 1052,1303 270,1303" fill="var(--paper)"/>
    <polygon class="back-red-corner" points="0,1040 275,1303 0,1303" fill="var(--brand-red)"/>
    <polygon class="back-red-band" points="432,1147 1052,1147 1052,1230 510,1230" fill="var(--brand-red)"/>

    <rect class="title-underline" x="130" y="843" width="97" height="6" fill="var(--brand-red)"/>

    <defs>
      <linearGradient id="portraitTone" x1="0" y1="0" x2="0" y2="1">
        <stop offset="0" stop-color="var(--photo-sky)"/>
        <stop offset="1" stop-color="var(--photo-green)"/>
      </linearGradient>
    </defs>
    <rect class="portrait-frame" x="125" y="889" width="276" height="225" fill="var(--brand-red)"/>
    <rect class="portrait" x="133" y="897" width="260" height="209" fill="url(#portraitTone)" role="img" aria-label="Portrait photo of the agent in a dark suit outdoors"/>

    <!-- phone icon -->
    <rect class="icon-tile" x="620" y="890" width="60" height="61" fill="var(--brand-red)"/>
    <rect x="638" y="899" width="24" height="43" rx="4" fill="none" stroke="var(--paper)" stroke-width="3"/>
    <line x1="640" y1="906" x2="660" y2="906" stroke="var(--paper)" stroke-width="2"/>
    <line x1="640" y1="933" x2="660" y2="933" stroke="var(--paper)" stroke-width="2"/>
    <circle cx="650" cy="937.5" r="1.8" fill="var(--paper)"/>

    <!-- mail icon -->
    <rect class="icon-tile" x="620" y="981" width="60" height="61" fill="var(--brand-red)"/>
    <rect x="630" y="998" width="40" height="28" fill="var(--paper)"/>
    <polyline points="630,998 650,1014 670,998" fill="none" stroke="var(--brand-red)" stroke-width="3"/>
    <line x1="630" y1="1026" x2="645" y2="1011" stroke="var(--brand-red)" stroke-width="2"/>
    <line x1="670" y1="1026" x2="655" y2="1011" stroke="var(--brand-red)" stroke-width="2"/>

    <!-- pin icon -->
    <rect class="icon-tile" x="620" y="1067" width="60" height="62" fill="var(--brand-red)"/>
    <path d="M650,1121 C642,1108 636,1100 636,1091 A14,14 0 0 1 664,1091 C664,1100 658,1108 650,1121 Z" fill="var(--paper)"/>
    <circle cx="650" cy="1091" r="5.5" fill="var(--brand-red)"/>

    <!-- globe icon -->
    <circle cx="649" cy="1190" r="31" fill="var(--paper)"/>
    <circle cx="649" cy="1190" r="24" fill="var(--brand-red)"/>
    <g fill="none" stroke="var(--paper)" stroke-width="2">
      <circle cx="649" cy="1190" r="14"/>
      <ellipse cx="649" cy="1190" rx="6" ry="14"/>
      <line x1="635" y1="1190" x2="663" y2="1190"/>
      <line x1="637" y1="1183" x2="661" y2="1183"/>
      <line x1="637" y1="1197" x2="661" y2="1197"/>
      <line x1="649" y1="1176" x2="649" y2="1204"/>
    </g>
  </svg>

  <div class="label brand-name front-brand">NURLO</div>
  <div class="label tagline front-tagline">Property Sold a Smarter Way...</div>

  <div class="label agent-name">LIAM PORTER</div>
  <div class="label agent-role">Licensed Real Estate Agent</div>

  <div class="label brand-name back-brand">NURLO</div>
  <div class="label tagline back-tagline">Property Sold a Smarter Way...</div>

  <div class="label contact contact-phone">0412 386 590</div>
  <div class="label contact contact-email">liam@nurlo.com</div>
  <div class="label contact contact-box">PO Box 7130</div>
  <div class="label contact contact-place">Harrowdale NSW 2790</div>
  <div class="label contact contact-web">www.nurlo.com</div>
</div>
</body>
</html>
```